High End Business Card Design for Flooring Store

Looking for a new card design for our hardwood flooring company. We have no print budget for these and are open to cards made from wood, metal, cardstock with embossed print ... or any combination of these. No plastic.

We sell luxury products and I want the cards to reflect our image of quality and class.

Our contact information as such;
Employee Name
418 Colbrook Blvd.
Larkfield, ON
K9R-3M5
(555) 214-3968
Employee email @velkaflooring.com

Target Market(s)

Home Builders

Contact Information for Business Card

Emnployee name, business contact information

```html
<!DOCTYPE html>
<html lang="en">
<head>
<meta charset="utf-8">
<title>Velka Flooring – Business Card</title>
<link href="https://fonts.googleapis.com/css2?family=Montserrat:wght@400;500;800&display=swap" rel="stylesheet">
<style>
  :root {
    --backdrop: #d4d5d7;
    --card-dark: #202020;
    --card-light: #ffffff;
    --brand-red: #9c2f28;
    --brand-gold: #e3ac26;
    --text-grey: #6f6f6f;
    --text-dark: #4a4a4a;
  }
  html, body {
    margin: 0;
    padding: 0;
    width: 900px;
    height: 1200px;
    overflow: hidden;
    background: var(--backdrop);
    font-family: "Montserrat", sans-serif;
  }
  .card {
    position: absolute;
    left: 134px;
    width: 632px;
    height: 361px;
  }
  .card-front {
    top: 212px;
    background: var(--card-dark);
  }
  .card-back {
    top: 628px;
    background: var(--card-light);
  }
  .brand {
    position: absolute;
    text-align: center;
  }
  .brand-name {
    display: flex;
    align-items: center;
    justify-content: center;
    gap: 14px;
    color: var(--brand-red);
    font-weight: 500;
    line-height: 1;
  }
  .brand-mark {
    display: inline-block;
    background: var(--brand-gold);
  }
  .brand-tagline {
    color: var(--text-grey);
    font-weight: 400;
    line-height: 1.12;
  }
  .card-front .brand {
    left: 0;
    right: 0;
    top: 118px;
  }
  .card-front .brand-name { font-size: 92px; letter-spacing: 1px; }
  .card-front .brand-mark { width: 44px; height: 44px; }
  .card-front .brand-tagline { font-size: 23px; margin-top: 6px; }

  .card-back .brand {
    left: 355px;
    width: 250px;
    top: 28px;
  }
  .card-back .brand-name { font-size: 60px; gap: 10px; }
  .card-back .brand-mark { width: 28px; height: 28px; }
  .card-back .brand-tagline { font-size: 17px; margin-top: 3px; color: var(--text-dark); }

  .person {
    position: absolute;
    left: 30px;
    top: 190px;
  }
  .person-name {
    margin: 0;
    font-size: 23px;
    font-weight: 800;
    letter-spacing: 1px;
    color: var(--brand-red);
  }
  .person-role {
    margin: 4px 0 0;
    font-size: 15px;
    color: var(--text-dark);
    letter-spacing: 0.5px;
  }
  .divider {
    position: absolute;
    left: 29px;
    right: 28px;
    top: 249px;
    height: 2px;
    background: var(--brand-gold);
  }
  .contact-list {
    position: absolute;
    left: 29px;
    top: 268px;
    margin: 0;
    padding: 0;
    list-style: none;
    font-size: 15px;
    letter-spacing: 0.8px;
    color: var(--text-dark);
  }
  .contact-list li {
    display: flex;
    align-items: center;
    height: 24.5px;
  }
  .contact-list svg {
    width: 17px;
    height: 17px;
    margin-right: 9px;
    fill: var(--brand-red);
  }
  .address {
    position: absolute;
    right: 28px;
    top: 268px;
    margin: 0;
    font-style: normal;
    text-align: right;
    font-size: 15px;
    letter-spacing: 0.6px;
    color: var(--text-dark);
    line-height: 24.5px;
  }
</style>
</head>
<body>

<section class="card card-front">
  <div class="brand">
    <div class="brand-name"><span class="brand-mark"></span>Velka</div>
    <div class="brand-tagline">Planchers &amp; Escaliers<br>Flooring &amp; Stairs</div>
  </div>
</section>

<section class="card card-back">
  <div class="brand">
    <div class="brand-name"><span class="brand-mark"></span>Velka</div>
    <div class="brand-tagline">Planchers &amp; Escaliers<br>Flooring &amp; Stairs</div>
  </div>

  <div class="person">
    <h1 class="person-name">ELISE MORROW</h1>
    <p class="person-role">Sales</p>
  </div>

  <div class="divider"></div>

  <ul class="contact-list">
    <li>
      <svg viewBox="0 0 24 24" aria-hidden="true"><path d="M6.6 10.8a15.1 15.1 0 0 0 6.6 6.6l2.2-2.2a1 1 0 0 1 1-.25 11.4 11.4 0 0 0 3.6.57 1 1 0 0 1 1 1V20a1 1 0 0 1-1 1A17 17 0 0 1 3 4a1 1 0 0 1 1-1h3.5a1 1 0 0 1 1 1c0 1.250.2 2.450.57 3.57a1 1 0 0 1-.25 1z"/></svg>
      (555) 214-3968
    </li>
    <li>
      <svg viewBox="0 0 24 24" aria-hidden="true"><path d="M2 5h20v2l-10 6L2 7z M2 9l10 6 10-6v10H2z"/></svg>
      emorrow@velkaflooring.com
    </li>
    <li>
      <svg viewBox="0 0 24 24" aria-hidden="true"><path d="M12 2a10 10 0 1 0 0 20 10 10 0 0 0 0-20zm6.9 6h-3a15 15 0 0 0-1.3-3.9A8 8 0 0 1 18.9 8zM12 4c.9 1.2 1.6 2.6 2 4h-4c.4-1.4 1.1-2.8 2-4zM4.3 14a8 8 0 0 1 0-4h3.4a16 16 0 0 0 0 4zm.8 2h3a15 15 0 0 0 1.3 3.9A8 8 0 0 1 5.1 16zm3-8h-3a8 8 0 0 1 4.3-3.9A15 15 0 0 0 8.1 8zM12 20c-.9-1.2-1.6-2.6-2-4h4c-.4 1.4-1.1 2.8-2 4zm2.3-6H9.7a14 14 0 0 1 0-4h4.6a14 14 0 0 1 0 4zm.3 5.9a15 15 0 0 0 1.3-3.9h3a8 8 0 0 1-4.3 3.9zm1.7-5.9a16 16 0 0 0 0-4h3.4a8 8 0 0 1 0 4z"/></svg>
      www.velkaflooring.com
    </li>
  </ul>

  <address class="address">
    418 Colbrook Blvd.<br>
    Larkfield, ON<br>
    K9R-3M5
  </address>
</section>

</body>
</html>
```